An innovative software company needs a business card!

We need a business card design for our new innovative software company. Please use the details for the business card provided in business card details section. We will use the business card paper like: https://www.prindlecard.example/us/products/nfc/business-cards-plus.html Our company name: celvane We have already a logo and colors to use in business cards too ,

Target Market(s)

App & Sofware Development

Industry/Entity Type

Software

Contact Information for Business Card

Lukas Brenner, BSc.
Owner and Creative Superhero

Adress:
Pelzerweg 14/3/1708
A - 1100, Wien

Tel: +43 (0) 664 219 53 08
Email: lukas.brenner@celvane.example
Web: www.celvane.example

Requirements
Must have
• - Use our logo
Nice to have
• It would be nice to have a nice picture on the backside. (About apps, software, technicals or funy stuff) - Use our colors as in business card (optional)

```html
<!DOCTYPE html>
<html lang="en">
<head>
<meta charset="utf-8">
<title>celvane business card</title>
<link rel="stylesheet" href="https://fonts.googleapis.com/css2?family=Montserrat:wght@400;500;700&display=swap">
<style>
  :root {
    --stage: #2e2e30;
    --card-black: #050505;
    --brand-blue: #14a4d6;
    --brand-grey: #c4c5c8;
    --text-white: #ffffff;
    --back-dark: #1c1d24;
  }
  * { margin: 0; padding: 0; box-sizing: border-box; }
  html, body { width: 1200px; height: 900px; overflow: hidden; }
  body {
    background: var(--stage);
    font-family: "Montserrat", Arial, sans-serif;
    position: relative;
  }
  .card {
    position: absolute;
    width: 560px;
    height: 350px;
    border-radius: 20px;
    overflow: hidden;
    box-shadow: 0 18px 40px rgba(0,0,0,0.55);
  }

  /* Back side */
  .card-back { left: 110px; top: 70px; background: var(--back-dark); }
  .back-visual {
    position: absolute; inset: 0;
    background:
      radial-gradient(ellipse at 30% 70%, rgba(150,30,50,0.55), transparent 55%),
      radial-gradient(ellipse at 75% 30%, rgba(40,50,110,0.6), transparent 55%),
      radial-gradient(ellipse at 20% 25%, rgba(120,130,40,0.35), transparent 45%),
      linear-gradient(135deg, #2a2b33, #15161d);
  }
  .back-brand {
    position: absolute; left: 110px; top: 118px;
    display: flex; align-items: center; gap: 22px;
  }
  .brand-dot {
    width: 70px; height: 70px; border-radius: 50%;
    background: var(--brand-grey);
    border: 4px solid var(--text-white);
  }
  .back-name {
    font-weight: 700; font-size: 84px; letter-spacing: -1px;
    color: var(--brand-blue); line-height: 1;
  }
  .back-url {
    position: absolute; left: 0; right: 0; top: 262px;
    text-align: center; font-size: 20px; font-weight: 500;
    color: var(--text-white); letter-spacing: 0.5px;
  }

  /* Front side */
  .card-front { left: 530px; top: 470px; background: var(--card-black); }
  .front-wave { position: absolute; inset: 0; }
  .front-brand {
    position: absolute; left: 34px; top: 74px;
    font-weight: 700; font-size: 70px; letter-spacing: -1px;
    color: var(--brand-blue); line-height: 1;
  }
  .front-dot {
    position: absolute; right: 40px; top: 26px;
    width: 84px; height: 84px; border-radius: 50%;
    background: var(--brand-grey);
    border: 4px solid var(--text-white);
  }
  .holder { position: absolute; left: 40px; top: 172px; color: var(--text-white); }
  .holder-name { font-size: 20px; font-weight: 500; color: var(--brand-blue); }
  .holder-role { font-size: 13px; margin-top: 2px; }
  .holder-address { font-size: 14px; margin-top: 16px; line-height: 1.45; }
  .contact {
    position: absolute; right: 24px; top: 226px;
    list-style: none; color: var(--text-white);
    font-size: 11.5px; text-align: right; line-height: 20px;
  }
  .contact li { display: flex; align-items: center; justify-content: flex-end; gap: 7px; }
  .contact strong { font-weight: 700; }
  .contact svg { width: 11px; height: 11px; flex: none; }
</style>
</head>
<body>

<section class="card card-back" aria-label="Card back">
  <div class="back-visual" role="img" aria-label="Abstract colourful tiled technology image in dark red, navy and yellow tones"></div>
  <div class="back-brand">
    <span class="brand-dot"></span>
    <span class="back-name">celvane</span>
  </div>
  <p class="back-url">www.celvane.example</p>
</section>

<section class="card card-front" aria-label="Card front">
  <svg class="front-wave" viewBox="0 0 560 350" aria-hidden="true">
    <path d="M0 300 C 300 320, 370 200, 420 0 L 560 0 L 560 350 L 0 350 Z" fill="var(--brand-blue)"/>
    <path d="M0 314 C 312 334, 382 214, 432 0 L 560 0 L 560 350 L 0 350 Z" fill="var(--card-black)"/>
    <path d="M0 320 C 318 340, 388 220, 438 0 L 560 0 L 560 350 L 0 350 Z" fill="var(--brand-grey)"/>
    <path d="M0 334 C 330 352, 400 232, 450 0 L 560 0 L 560 350 L 0 350 Z" fill="var(--card-black)"/>
    <path d="M20 350 C 336 350, 403 236, 453 0 L 560 0 L 560 350 Z" fill="var(--brand-blue)"/>
  </svg>
  <span class="front-dot"></span>
  <div class="front-brand">celvane</div>
  <div class="holder">
    <p class="holder-name">Lukas Brenner, BSc</p>
    <p class="holder-role">Owner and Creative Superhero</p>
    <p class="holder-address">Pelzerweg 14/3/1708<br>A - 1100, Wien</p>
  </div>
  <ul class="contact">
    <li><span>+43 (0) 664 219 53 08</span>
      <svg viewBox="0 0 24 24" aria-hidden="true"><path fill="#fff" d="M6.6 10.8a15 15 0 0 0 6.6 6.6l2.2-2.2c.3-.3.7-.4 1-.2 1.1.4 2.3.6 3.6.6.6 0 1 .4 1 1V20c0 .6-.4 1-1 1A17 17 0 0 1 3 4c0-.6.4-1 1-1h3.5c.6 0 1 .4 1 1 0 1.3.2 2.5.6 3.6.1.3 0 .7-.2 1z"/></svg>
    </li>
    <li><span>www.<strong>celvane</strong>.example</span>
      <svg viewBox="0 0 24 24" aria-hidden="true"><circle cx="12" cy="12" r="9" fill="none" stroke="#fff" stroke-width="2"/><path d="M3 12h18M12 3c3 3 3 15 0 18M12 3c-3 3-3 15 0 18" fill="none" stroke="#fff" stroke-width="1.6"/></svg>
    </li>
    <li><span>lukas.brenner@celvane.example</span>
      <svg viewBox="0 0 24 24" aria-hidden="true"><rect x="3" y="5" width="18" height="14" rx="1" fill="none" stroke="#fff" stroke-width="2"/><path d="M3 6l9 7 9-7" fill="none" stroke="#fff" stroke-width="2"/></svg>
    </li>
  </ul>
</section>

</body>
</html>
```